Word Doc Design for construction report

We have a database that dumps all of this data into this word doc. We need a much more appealing, visually friendly document. I have attached the main document and the cover page.
You don't need to edited all the repeated pages, just give us a style guide. I have attached our branding.
Updates

Hi I have pulled together a final design and now just need someone to put it all into a word doc. The final document is 36 pages. I am prepared to pay the design fee listed plus a $200 tip, however, we need it delivered by Monday. Is there anyone available to do this work?

Requirements
Must have
• Be easy on the eye as there is a LOT of repeated content

```html
<!DOCTYPE html>
<html lang="en">
<head>
<meta charset="utf-8">
<title>Strata Maintenance Report – Style Pages</title>
<link href="https://fonts.googleapis.com/css2?family=Didact+Gothic&family=Exo+2:wght@300;400&display=swap" rel="stylesheet">
<style>
:root{
  --blue:#1b93d3;
  --teal:#1fa597;
  --navy:#2b3a8c;
  --ink:#1d1d1b;
  --grey:#8a8a8a;
  --frame:#6f6f6f;
  --paper:#ffffff;
}
*{box-sizing:border-box;margin:0;padding:0}
html,body{width:1200px;height:1200px;overflow:hidden;background:var(--paper)}
body{position:relative;font-family:"Didact Gothic",sans-serif;color:var(--ink)}
.page{position:absolute;top:211px;width:556px;height:787px;border:1px solid var(--frame);background:var(--paper);overflow:hidden}
.page--one{left:26px}
.page--two{left:599px}
.corner-band{position:absolute;height:10px}
.corner-band--top{right:0;top:0;width:208px;background:linear-gradient(90deg,rgba(31,165,151,.35),rgba(27,147,211,.55))}
.corner-band--bottom{left:0;bottom:0;width:204px;background:linear-gradient(90deg,rgba(27,147,211,.55),rgba(31,165,151,.35))}
.brand{position:absolute;left:33px;top:34px;display:flex;align-items:center;gap:5px;font-family:"Exo 2",sans-serif;font-weight:400;font-size:14px;color:var(--navy)}
.brand__square{width:8px;height:8px;background:var(--navy)}
.portal{position:absolute;left:32px;top:93px;width:499px;height:111px;background:var(--blue);color:#fff;padding:4px 5px}
.portal h1{font-family:"Exo 2",sans-serif;font-weight:300;font-size:14.5px;margin-bottom:9px}
.portal p{font-family:"Exo 2",sans-serif;font-weight:300;font-size:9.2px;line-height:13.4px;text-align:justify;letter-spacing:.1px}
.summary-tab{position:absolute;left:26px;top:224px;width:166px;height:31px;background:var(--blue);clip-path:polygon(6% 0,100% 0,94% 100%,0 100%);color:#fff;font-family:"Exo 2",sans-serif;font-weight:300;font-size:15px;line-height:31px;padding-left:10px}
.details{position:absolute;left:57px;top:265px;font-size:9.4px;line-height:13.4px;border-collapse:collapse}
.details td{padding:0;height:13.4px;vertical-align:top}
.details td:first-child{width:138px}
.details .gap td{height:13.4px}
.body-copy{position:absolute;left:37px;width:481px;font-size:9.2px;line-height:13.4px;text-align:justify}
.body-copy--a{top:436px}
.body-copy--b{top:544px}
.footer{position:absolute;right:25px;top:746px;text-align:right;font-size:8px;line-height:12px}
.footer__page{color:var(--grey);font-size:9px}
.footer__copy{color:var(--blue);font-size:7.5px}
.scope{position:absolute;left:37px;top:96px;width:481px;font-size:9.2px;line-height:13.4px}
.scope h2{font-family:"Exo 2",sans-serif;font-weight:300;font-size:11.4px;letter-spacing:-.15px;color:var(--teal);line-height:15px;white-space:nowrap}
.scope p{text-align:justify}
.scope ul{list-style:none}
.scope li{position:relative;text-indent:34px;text-align:justify}
.scope li::before{content:"";position:absolute;left:2px;top:5px;width:3.5px;height:3.5px;border-radius:50%;background:var(--teal)}
.scope .legislation li{text-indent:44px}
.scope .legislation li::before{left:36px}
.important{position:absolute;left:37px;top:376px;width:481px;font-size:9.2px;line-height:13.4px;text-align:justify}
.important strong{font-family:"Exo 2",sans-serif;font-weight:300;font-size:12px;color:var(--blue)}
.thanks{position:absolute;left:37px;top:470px;font-size:9.2px}
.signature{position:absolute;left:37px;top:511px;font-size:9.2px;line-height:13.4px}
.charity{position:absolute;left:45px;top:598px;display:flex;align-items:center;gap:6px;font-family:"Didact Gothic",sans-serif;font-size:21px;color:var(--teal)}
.charity__dot{width:14px;height:14px;border-radius:50%;background:var(--blue)}
.charity-note{position:absolute;left:51px;top:655px;width:158px;font-size:7.4px;line-height:9.4px;text-align:justify;letter-spacing:.3px}
.badge-association{position:absolute;left:246px;top:589px;width:137px;height:55px;border:2px solid #c9c76a;background:#17803a}
.badge-member{position:absolute;left:424px;top:573px;width:64px;height:64px;background:#f0932b}
</style>
</head>
<body>

<section class="page page--one">
  <div class="corner-band corner-band--top" role="img" aria-label="Decorative brand-colour corner accent"></div>
  <div class="corner-band corner-band--bottom" role="img" aria-label="Decorative brand-colour corner accent"></div>
  <div class="brand"><span class="brand__square"></span>Harbourline Reports</div>

  <div class="portal">
    <h1>Harbourline Reports Strata Maintenance Portal</h1>
    <p>Your Strata Manager at [[X Strata Group]] and the Executive Committee for the Owners Corporation have been provided with access to the Harbourline Reports Strata Maintenance Portal BuildVault. This powerful building management resource provides access to the Building File for [[StreetAddress]] [[Suburb]] and includes a comprehensive photo log, your Maintenance Plan, Anticipated Capital Expenditure Plan and important maintenance logs and service reminders on the common property.</p>
  </div>

  <div class="summary-tab">REPORT SUMMARY</div>

  <table class="details">
    <tr><td>CLIENT</td><td>[[ClientName]]</td></tr>
    <tr><td>BUILDING LOCATION</td><td>[[StreetAddress]] [[Suburb]]</td></tr>
    <tr><td>BLOCK NUMBER</td><td>[[BLOCK]]</td></tr>
    <tr><td>SECTION NUMBER</td><td>[[SECTION]]</td></tr>
    <tr><td>SCHEME NUMBER</td><td></td></tr>
    <tr class="gap"><td></td><td></td></tr>
    <tr><td>INSPECTION DATE</td><td>[[InspectionDate@d mmmm yyyy]]</td></tr>
    <tr><td>INSPECTOR</td><td>[[Inspector]]</td></tr>
    <tr><td>WEATHER CONDITIONS</td><td>[[Summary of Property Details|weather conditions|ItemValue]]</td></tr>
    <tr class="gap"><td></td><td></td></tr>
    <tr><td>BUILDVAULT FILE NUMBER</td><td>[[JobNumber]]</td></tr>
  </table>

  <p class="body-copy body-copy--a">The Unit Titles (Management) Act 2011 and associated regulations provides the framework for the management of multi-unit residential properties. All Owners Corporations are required to hold a Maintenance Plan, taking into account the Developers Maintenance Schedule (if any). The Executive Committee then references this plan as part of their responsibility for overseeing the maintenance of the common property. The Owners Corporation should regularly review their maintenance plan and amend when necessary. A comprehensive database relating to the maintenance, repair or replacement undertaken to any systems, equipment, structures and other items on the common property, including copies of manuals and warranty information is registered in BuildVault for this building.</p>

  <p class="body-copy body-copy--b">Following the preparation of our project file for [[StreetAddress]] [[Suburb]] which included referencing materials such as maintenance schedules, sinking fund reports, warranties, manufacturer's recommendations, and specific product information provided to us, our Building Inspector conducted a comprehensive on-site visual inspection on [[InspectionDate@d mmmm yyyy]]. If detailed information regarding plant and equipment and common areas was not made available to us, or visually evident on the day of inspection, the BuildVault file for this building will be updated by [[X strata manager]] and the Executive Committee as required. It is critical that this Maintenance Plan is monitored and updated on an ongoing basis to ensure the optimum working condition of systems, equipment, structures and other elements of the common property and to avoid costly reactive repairs.</p>

  <div class="footer">
    <div class="footer__page">Page 1</div>
    <div class="footer__copy">[[StreetAddress]] [[Suburb]] - COPYRIGHT: Harbourline Reports</div>
  </div>
</section>

<section class="page page--two">
  <div class="corner-band corner-band--top" role="img" aria-label="Decorative brand-colour corner accent"></div>
  <div class="corner-band corner-band--bottom" role="img" aria-label="Decorative brand-colour corner accent"></div>
  <div class="brand"><span class="brand__square"></span>Harbourline Reports</div>

  <div class="scope">
    <h2>Project Scope</h2>
    <p>This Maintenance Plan has been compiled to assist the Property to meet their obligations with respect to the following legislation (both as amended 1 November 2020):</p>
    <ul class="legislation">
      <li>Unit Titles (Management) Act 2011 (s24);</li>
      <li>Unit Titles (Management) Regulation 2011 (s4A)</li>
    </ul>
    <h2>Documents supplied as part of the Developer's Maintenance Schedule and other reference material</h2>
    <ul>
      <li>Drop downs</li>
      <li>Civic Services Bureau Multi-unit Residential Building Maintenance Guide</li>
    </ul>
    <h2>Manuals, warranties and sundry maintenance statements</h2>
    <ul>
      <li>All documentation supplied by the Strata Group that has been referenced during the compilation of this Maintenance Plan has been saved against the Strata File in the Harbourline Reports Strata Maintenance Portal.</li>
    </ul>
    <h2>Building Class</h2>
    <ul><li>X</li></ul>
    <p>In typical Class A Units Plans, the unit owner owns the inside of the unit but not the main structure of the building. Usually, the individual owner owns from the inside of their lot to halfway out through the boundary walls, ceiling, and the floor. In general, the owners corporation owns the walls, ceiling and floor from outside of the lot to halfway in. The internal walls within the unit (e.g. the wall between the kitchen and lounge room), floor coverings, light fittings and curtains are all the property of the unit owner.</p>
  </div>

  <p class="important"><strong>IMPORTANT:</strong> This report is intended to be read in its entirety. It has been commissioned to satisfy the requirements of 4A Maintenance plan &nbsp; Act, s 24 (3), Unit Titles Management Regulation 2011. The appropriate Strata Group Representative or Members of the Body Corporate Executive are requested to immediately contact our company if any of the report's content is not fully understood and requires clarification or further explanation.<br>Please refer to important Scope and Limitations at the end of this document.</p>

  <p class="thanks">Thank you for the opportunity to work with you on this project, please do not hesitate to contact our team.</p>

  <p class="signature">[[Summary of Property Details|SIGNATURE|image100@100]]<br>[[Summary of Property Details|SIGNATURE|itemvalue]]</p>

  <div class="charity"><span class="charity__dot"></span>Open Door Fund</div>
  <p class="charity-note">A percentage from every inspection contributes to our in house charity, supporting those in our community who do not have a place to call home. Visit our website to learn more.</p>

  <div class="badge-association" role="img" aria-label="Industry association membership badge"></div>
  <div class="badge-member" role="img" aria-label="Builders association member badge"></div>

  <div class="footer">
    <div class="footer__page">Page 2</div>
    <div class="footer__copy">[[StreetAddress]] [[Suburb]] - COPYRIGHT: Harbourline Reports</div>
  </div>
</section>

</body>
</html>
```